STATIONERY and Brand ID for KelvaBank

We need a family of identical Brand guide
Call Card
Envelope
Letterhead
Poster
Brochure

It needs to have an international Fee/

The ARCHITECTURE/STRUCTURE must show the highest level of creativity

1. Call card could be two sided
2. cal card can have a a flap
3. Call card can have a curved edge

Target Market(s)

Business and bank clients

Industry/Entity Type

Bank

Requirements
Must have
• the logo atatched
• the colour scheme must be used
• There must be a common look and feel and they must have the same DNA

```html
<!DOCTYPE html>
<html lang="en">
<head>
<meta charset="utf-8">
<title>KelvaBank Stationery</title>
<link href="https://fonts.googleapis.com/css2?family=Arimo:wght@400;700&display=swap" rel="stylesheet">
<style>
  :root {
    --navy: #283069;
    --green: #7db43c;
    --paper: #ffffff;
    --envelope: #f4f4f5;
    --backdrop: #e4e4e6;
    --ink: #1c1c22;
  }
  * { box-sizing: border-box; margin: 0; padding: 0; }
  html, body { width: 1200px; height: 960px; overflow: hidden; }
  body { background: var(--backdrop); font-family: "Arimo", Arial, sans-serif; color: var(--ink); position: relative; }

  .sheet { position: absolute; box-shadow: 0 6px 18px rgba(0,0,0,.12); }

  .brand { display: flex; align-items: center; gap: 10px; }
  .brand-dot { width: 14px; height: 14px; border-radius: 50%; background: var(--green); flex: none; }
  .brand-name { font-weight: 700; color: var(--navy); letter-spacing: -0.5px; line-height: 1; white-space: nowrap; }

  .contact-list { list-style: none; text-align: right; }
  .contact-list li { display: flex; justify-content: flex-end; align-items: center; gap: 8px; white-space: nowrap; }
  .contact-list svg { fill: var(--green); flex: none; }

  /* Letterhead */
  .letterhead { left: 50px; top: 40px; width: 470px; height: 665px; background: var(--paper); }
  .letterhead .side-band { position: absolute; left: 22px; top: 0; bottom: 0; width: 10px; background: var(--navy); }
  .letterhead .brand { position: absolute; left: 70px; top: 52px; }
  .letterhead .brand-name { font-size: 44px; }
  .letterhead .contact-list { position: absolute; right: 32px; top: 170px; font-size: 10px; line-height: 17px; }
  .letterhead .footer-rule { position: absolute; left: 60px; right: 40px; bottom: 60px; height: 2px; background: var(--navy); }
  .letterhead .footer-address { position: absolute; left: 0; right: 0; bottom: 36px; text-align: center; font-size: 10px; }

  /* Business cards */
  .card { width: 340px; height: 195px; }
  .card-back { left: 690px; top: 40px; background: var(--paper); }
  .card-back .side-band { position: absolute; left: 0; top: 0; bottom: 0; width: 26px; background: var(--navy); display: flex; flex-direction: column; justify-content: center; align-items: center; gap: 9px; }
  .card-back .side-band svg { fill: var(--green); }
  .card-back .person { position: absolute; left: 44px; top: 28px; font-size: 12px; line-height: 15px; }
  .card-back .person strong { display: block; }
  .card-back .details { position: absolute; left: 44px; top: 78px; font-size: 9.5px; line-height: 14px; }
  .card-back .brand { position: absolute; right: 18px; bottom: 20px; gap: 6px; }
  .card-back .brand-name { font-size: 22px; }
  .card-back .brand-dot { width: 8px; height: 8px; }

  .card-front { left: 690px; top: 265px; background: var(--navy); display: flex; align-items: center; justify-content: center; overflow: hidden; }
  .card-front .brand { gap: 8px; }
  .card-front .brand-name { font-size: 34px; color: var(--paper); }

  /* Envelope */
  .envelope { left: 560px; top: 520px; width: 600px; height: 400px; background: var(--envelope); }
  .envelope .brand { position: absolute; left: 40px; top: 38px; }
  .envelope .brand-name { font-size: 42px; }
  .envelope .address-window { position: absolute; left: 40px; top: 130px; width: 300px; height: 110px; border: 1.5px solid var(--ink); border-radius: 12px; }
  .envelope .side-band { position: absolute; right: 24px; top: 0; bottom: 0; width: 18px; background: var(--navy); }
  .envelope .contact-list { position: absolute; right: 56px; bottom: 40px; font-size: 15px; line-height: 26px; }
</style>
</head>
<body>

<section class="sheet letterhead" aria-label="Letterhead">
  <div class="side-band"></div>
  <div class="brand">
    <span class="brand-name">KelvaBank</span>
    <span class="brand-dot"></span>
  </div>
  <ul class="contact-list">
    <li>(123) 345-6789 <svg width="9" height="9" viewBox="0 0 24 24"><path d="M6.6 10.8a15 15 0 0 0 6.6 6.6l2.2-2.2a1 1 0 0 1 1-.3 11 11 0 0 0 3.6.6 1 1 0 0 1 1 1V20a1 1 0 0 1-1 1A17 17 0 0 1 3 4a1 1 0 0 1 1-1h3.5a1 1 0 0 1 1 1c0 1.3.2 2.5.6 3.6a1 1 0 0 1-.3 1z"/></svg></li>
    <li>hello@kelvabank.co.uk <svg width="9" height="9" viewBox="0 0 24 24"><path d="M2 5h20v14H2zm2 2v.5l8 5 8-5V7l-8 5z"/></svg></li>
    <li>www.kelvabank.co.uk <svg width="9" height="9" viewBox="0 0 24 24"><circle cx="12" cy="12" r="9" fill="none" stroke="#7db43c" stroke-width="2.5"/></svg></li>
  </ul>
  <div class="footer-rule"></div>
  <p class="footer-address">1234, your street City, ST12345</p>
</section>

<section class="sheet card card-back" aria-label="Business card, contact side">
  <div class="side-band">
    <svg width="9" height="9" viewBox="0 0 24 24"><path d="M12 2a7 7 0 0 0-7 7c0 5 7 13 7 13s7-8 7-13a7 7 0 0 0-7-7zm0 9.5A2.5 2.5 0 1 1 12 6.5a2.5 2.5 0 0 1 0 5z"/></svg>
    <svg width="9" height="9" viewBox="0 0 24 24"><path d="M6.6 10.8a15 15 0 0 0 6.6 6.6l2.2-2.2a1 1 0 0 1 1-.3 11 11 0 0 0 3.6.6 1 1 0 0 1 1 1V20a1 1 0 0 1-1 1A17 17 0 0 1 3 4a1 1 0 0 1 1-1h3.5a1 1 0 0 1 1 1c0 1.3.2 2.5.6 3.6a1 1 0 0 1-.3 1z"/></svg>
    <svg width="9" height="9" viewBox="0 0 24 24"><path d="M2 5h20v14H2zm2 2v.5l8 5 8-5V7l-8 5z"/></svg>
    <svg width="9" height="9" viewBox="0 0 24 24"><circle cx="12" cy="12" r="9" fill="none" stroke="#7db43c" stroke-width="2.5"/></svg>
  </div>
  <div class="person"><strong>Your Name</strong>Position</div>
  <div class="details">
    1234, your street<br>City, ST12345<br>(123) 345-6789<br>hello@kelvabank.co.uk<br>www.kelvabank.co.uk
  </div>
  <div class="brand">
    <span class="brand-name">KelvaBank</span>
    <span class="brand-dot"></span>
  </div>
</section>

<section class="sheet card card-front" aria-label="Business card, brand side">
  <div class="brand">
    <span class="brand-name">KelvaBank</span>
    <span class="brand-dot"></span>
  </div>
</section>

<section class="sheet envelope" aria-label="Window envelope">
  <div class="brand">
    <span class="brand-name">KelvaBank</span>
    <span class="brand-dot"></span>
  </div>
  <div class="address-window"></div>
  <ul class="contact-list">
    <li>(123) 345-6789 <svg width="12" height="12" viewBox="0 0 24 24"><path d="M6.6 10.8a15 15 0 0 0 6.6 6.6l2.2-2.2a1 1 0 0 1 1-.3 11 11 0 0 0 3.6.6 1 1 0 0 1 1 1V20a1 1 0 0 1-1 1A17 17 0 0 1 3 4a1 1 0 0 1 1-1h3.5a1 1 0 0 1 1 1c0 1.3.2 2.5.6 3.6a1 1 0 0 1-.3 1z"/></svg></li>
    <li>hello@kelvabank.co.uk <svg width="12" height="12" viewBox="0 0 24 24"><path d="M2 5h20v14H2zm2 2v.5l8 5 8-5V7l-8 5z"/></svg></li>
    <li>www.kelvabank.co.uk <svg width="12" height="12" viewBox="0 0 24 24"><circle cx="12" cy="12" r="9" fill="none" stroke="#7db43c" stroke-width="2.5"/></svg></li>
  </ul>
  <div class="side-band"></div>
</section>

</body>
</html>
```